Report-Design  für Social-Media-Beratungs-Agentur
Report-Design für Social-Media-Beratungs-Agentur
Zielgruppe
Wir sind eine Social-Media-Beratungs-Agentur, die KMU bei der strategischen Ausrichtung und Umsetzung ihrer Social-Media-Präsenzen berät und unterstützt.
Aufgabenstellung
Wir analysieren die KarriNetz Profile von Unternehmen in einer Excel-Datei, indem wir in einem Reiter verschiedene Aspekte bewerten. Aus diesen Bewertungen ergibt sich dann in einem zweiten Reiter ein Report (hängt hier an), in den die Ergebnisse aus der 1. Mappe automatisch übernommen werden. Dieser Report wird als PDF gespeichert und an den Kunden geschickt. Wir möchten das Report-Design gerne neu gestalten lassen: Es soll zeitgemäß, professionell und kompetent wirken und nicht mehr 'wie in Excel zusammengebastelt'. Ein Beispiel für ein Design, das uns gefällt, hängt als Inspiration an. Gerne können Grafikelemente aus Canva oder anderen Grafikprogrammen eingefügt werden. Wichtig ist, dass die Struktur mit den Zellen, in die Daten automatisch übernommen werden (im Anhang durch # gekennzeichnet), erhalten bleibt. Unsere Firmenfarben sind: #f69f25, #11323a, #809398, #fcfefd. Wir haben noch weitere Analysen, die wir bei Erfolg dieses Auftrags ebenfalls gerne optimieren lassen möchten.

```html
<!DOCTYPE html>
<html lang="de">
<head>
<meta charset="utf-8">
<title>Kavenor – Profilanalyse Report</title>
<link href="https://fonts.googleapis.com/css2?family=Montserrat:wght@400;500;700;800&display=swap" rel="stylesheet">
<style>
:root{
  --orange:#f69f25;
  --navy:#11323a;
  --deep:#04343f;
  --slate:#809398;
  --paper:#fcfefd;
  --ink:#3a3a3a;
  --backdrop:#b3b3b3;
  --line:#f6b25a;
}
*{margin:0;padding:0;box-sizing:border-box}
html,body{width:1200px;height:1117px;overflow:hidden;background:var(--backdrop);font-family:'Montserrat',sans-serif}
.report{position:absolute;left:220px;top:20px;width:1158px;height:1640px;background:#fff;transform:scale(.6567);transform-origin:0 0;overflow:hidden;box-shadow:0 20px 40px rgba(0,0,0,.25)}
.abs{position:absolute}
.hero-photo{left:0;top:37px;width:1158px;height:433px;background:linear-gradient(100deg,#5d5f60 0%,#4a4c4d 35%,#5a5b5c 60%,#b9bbbd 78%,#8f9193 100%)}
.logo-tab{left:0;top:37px}
.brand{left:370px;top:48px;width:420px;text-align:center}
.brand-name{font-weight:500;font-size:66px;letter-spacing:-1px;color:var(--navy);line-height:1}
.brand-sub{display:flex;align-items:center;justify-content:center;gap:12px;margin-top:6px;font-weight:700;font-size:23px;color:var(--navy)}
.brand-sub .mark{width:18px;height:18px;background:var(--navy)}
.hero-title{left:108px;top:258px;color:#fff;font-weight:800;font-size:41px;line-height:44px}
.hero-sub{left:108px;top:355px;color:#fff;font-weight:700;font-size:22px;line-height:32px}
.meta-pill{left:222px;top:445px;width:716px;height:56px;border-radius:28px;background:var(--deep);box-shadow:0 6px 8px rgba(0,0,0,.12);display:flex;align-items:center;font-size:23px;color:#fff}
.meta-pill .author{padding-left:30px;flex:1}
.meta-pill .date{background:var(--orange);height:100%;border-radius:28px;padding:0 22px;display:flex;align-items:center}
.goal-title{left:108px;top:665px;color:var(--orange);font-weight:800;font-size:30px}
.goal-text{left:107px;top:726px;width:340px;font-size:19.5px;line-height:29.6px;color:var(--ink)}
.goal-text p+p{margin-top:29.6px}
.goal-rule{left:223px;top:1173px;width:92px;height:5px;background:var(--orange)}
.timeline{left:0;top:0}
.item-title{left:612px;color:var(--orange);font-weight:800;font-size:19px}
.item-text{left:612px;width:450px;font-size:17px;line-height:24.5px;color:var(--ink)}
.rec-band{left:0;top:1333px;width:1158px;height:195px;background:var(--deep)}
.rec-banner{left:62px;top:1305px;width:1034px;height:56px;background:var(--orange);color:#fff;font-weight:800;font-size:25px;padding-left:46px;line-height:58px}
.rec{top:1382px;width:270px;color:#fff;font-weight:700;font-size:17.5px;line-height:24.5px}
.tick{top:1384px}
.rec-note{left:0;top:1468px;width:1158px;text-align:center;color:#fff;font-size:11.5px;line-height:16.5px}
.contact{top:1555px;font-size:17.5px;line-height:25px;color:var(--ink)}
.divider{top:1548px;width:1px;height:52px;background:var(--orange)}
</style>
</head>
<body>
<main class="report">
  <div class="abs hero-photo" role="img" aria-label="Fotografie: Schreibtisch von oben mit Notizblock, Zimmerpflanze und Händen auf einer Laptop-Tastatur"></div>
  <svg class="abs logo-tab" width="1158" height="140" viewBox="0 0 1158 140">
    <path d="M300 0 C340 0 345 20 360 50 C385 115 400 135 450 135 L720 135 C770 135 785 115 810 50 C825 20 830 0 870 0 Z" fill="#fff"/>
  </svg>
  <div class="abs brand">
    <div class="brand-name">KAVENOR</div>
    <div class="brand-sub"><span class="mark"></span>social media beratung</div>
  </div>

  <h1 class="abs hero-title">OPTIMIEREN SIE IHRE<br>SOCIAL-MEDIA-NUTZUNG</h1>
  <p class="abs hero-sub">STRATEGISCHER ANSATZ. ZEITSPARENDE<br>REDAKTION MIT KI. ECHTE ERGEBNISSE.</p>
  <div class="abs meta-pill"><span class="author">Erstellt durch: <b>Marlene Hofer</b></span><span class="date">Datum:&nbsp;<b>23.07.2025</b></span></div>

  <h2 class="abs goal-title">ZIEL DER ANALYSE</h2>
  <div class="abs goal-text">
    <p>Diese Analyse zeigt, wie gut Ihr KarriNetz-Unternehmensprofil die Potenziale von Social Media bereits nutzt - und wo noch ungenutzte Chancen liegen.</p>
    <p>Hohe Werte bedeuten echten Mehrwert für Ihr Unternehmen, niedrigere Werte viel Potenzial für mehr Sichtbarkeit &amp; Wirkung. Am Ende erhalten Sie konkrete Empfehlungen, mit denen Sie sofort an den richtigen Stellschrauben drehen können.</p>
  </div>
  <div class="abs goal-rule"></div>

  <svg class="abs timeline" width="1158" height="1300" viewBox="0 0 1158 1300">
    <defs>
      <polygon id="hex" points="0,-46 40,-23 40,23 0,46 -40,23 -40,-23" fill="#f69f25"/>
    </defs>
    <g stroke="#f69f25" stroke-width="2" fill="none">
      <path d="M454 590 V1221"/>
      <path d="M454 590 H494 M454 744 H494 M454 895 H494 M454 1076 H494 M454 1221 H494"/>
    </g>
    <g fill="#f69f25"><circle cx="494" cy="590" r="3.5"/><circle cx="494" cy="744" r="3.5"/><circle cx="494" cy="895" r="3.5"/><circle cx="494" cy="1076" r="3.5"/><circle cx="494" cy="1221" r="3.5"/></g>
    <g stroke="#f6b25a" stroke-width="1.5" stroke-dasharray="5 4">
      <path d="M454 670 H1050 M454 825 H1050 M454 1000 H1050 M454 1150 H1050"/>
    </g>
    <use href="#hex" x="546" y="591"/>
    <use href="#hex" x="546" y="744"/>
    <use href="#hex" x="546" y="895"/>
    <use href="#hex" x="546" y="1076"/>
    <use href="#hex" x="546" y="1220"/>
    <g stroke="#fff" stroke-width="3" fill="none" stroke-linecap="round" stroke-linejoin="round">
      <circle cx="546" cy="576" r="8"/><path d="M528 614 V604 Q528 592 546 592 Q564 592 564 604 V614 Z"/>
      <rect x="522" y="724" width="28" height="24" rx="2"/><circle cx="552" cy="738" r="7"/><path d="M538 768 V760 Q538 750 552 750 Q566 750 566 760 V768 Z M526 760 H534"/>
      <path d="M560 888 A20 20 0 1 1 552 876"/><path d="M552 892 A8 8 0 1 1 546 887"/><path d="M546 895 L566 875 M560 873 L566 875 L568 881"/>
      <path d="M530 1056 H554 L562 1064 V1096 H530 Z M537 1070 H554 M537 1078 H550 M537 1086 H546"/><path d="M552 1092 L570 1068 L575 1072 L557 1096 Z"/>
      <path d="M536 1228 Q528 1220 530 1208 Q534 1194 546 1194 Q558 1194 562 1208 Q564 1220 556 1228 V1236 H536 Z M538 1242 H554"/>
      <path d="M550 1204 Q546 1200 542 1204 Q542 1210 546 1210 Q550 1210 550 1216 Q546 1220 542 1216 M546 1200 V1222"/>
      <path d="M520 1206 H524 M568 1206 H572 M524 1190 L527 1193 M568 1190 L565 1193"/>
    </g>
  </svg>

  <h3 class="abs item-title" style="top:541px">LOREM IPSUM DOLOR SIT AMET</h3>
  <p class="abs item-text" style="top:578px">Diese Zahl bewertet, ob Ihr Profil sauber aufgesetzt ist und alle wichtigen Informationen ansprechend für Ihre Zielgruppe eingepflegt sind.</p>
  <h3 class="abs item-title" style="top:695px">LOREM IPSUM DOLOR SIT AMET</h3>
  <p class="abs item-text" style="top:733px">Wir dürfen keine Rechtsberatung leisten. Dennoch haben wir geprüft, ob Ihr Profil die wichtigsten rechtlichen ichtlinien beachtet.</p>
  <h3 class="abs item-title" style="top:846px">LOREM IPSUM DOLOR SIT AMET</h3>
  <p class="abs item-text" style="top:881px;width:400px">Veröffentlichen Sie regelmäßig für die Zielgruppe interessante Beiträge? Sind die Beitragstexte und Bilder gut lesbar und aussagekräftig?</p>
  <h3 class="abs item-title" style="top:1024px">LOREM IPSUM DOLOR SIT AMET</h3>
  <p class="abs item-text" style="top:1057px">Diese Zahl bewertet die Anzahl Ihrer Followersowie die Resonanz zu Ihrem Profil und Ihren veröffentlichten Beiträgen auf KarriNetz.</p>
  <h3 class="abs item-title" style="top:1175px">LOREM IPSUM DOLOR SIT AMET</h3>
  <p class="abs item-text" style="top:1209px;width:380px">Consectetur adipiscing elit. Suspendisse venenatis dolor ac eleifend eleifend.</p>

  <div class="abs rec-band"></div>
  <h2 class="abs rec-banner">DREI EMPFEHLUNGEN FÜR EINEN GRÖẞEREN ERFOLG IHRER SEITE</h2>
  <svg class="abs tick" style="left:109px" width="20" height="20" viewBox="0 0 20 20"><circle cx="10" cy="10" r="9" fill="#f69f25"/><path d="M6 10 L9 13 L14 7" stroke="#fff" stroke-width="2.2" fill="none"/></svg>
  <p class="abs rec" style="left:152px">Consectetur adipiscing elit. Suspendisse venenatis dolor ac eleifend eleifend.</p>
  <svg class="abs tick" style="left:439px" width="20" height="20" viewBox="0 0 20 20"><circle cx="10" cy="10" r="9" fill="#f69f25"/><path d="M6 10 L9 13 L14 7" stroke="#fff" stroke-width="2.2" fill="none"/></svg>
  <p class="abs rec" style="left:476px">Consectetur adipiscing elit. Suspendisse venenatis dolor ac eleifend eleifend.</p>
  <svg class="abs tick" style="left:760px" width="20" height="20" viewBox="0 0 20 20"><circle cx="10" cy="10" r="9" fill="#f69f25"/><path d="M6 10 L9 13 L14 7" stroke="#fff" stroke-width="2.2" fill="none"/></svg>
  <p class="abs rec" style="left:800px">Consectetur adipiscing elit. Suspendisse venenatis dolor ac eleifend eleifend.</p>
  <p class="abs rec-note">Gerne erläutern wir Ihnen die Details hinter der Analyse und den Empfehlungen in einem Telefonat oder einer Videokonferenz.<br>Bei Fragen können Sie sich gerne bei uns melden!</p>

  <svg class="abs" style="left:108px;top:1550px" width="22" height="22" viewBox="0 0 22 22"><path d="M11 1 C5 1 2 5 2 9 C2 15 11 21 11 21 C11 21 20 15 20 9 C20 5 17 1 11 1 Z" fill="#f69f25"/><circle cx="11" cy="9" r="3.5" fill="#fff"/></svg>
  <p class="abs contact" style="left:149px">Social-Media-Beratung<br>Lindenweg 12 79100 Freiburg</p>
  <div class="abs divider" style="left:455px"></div>
  <svg class="abs" style="left:530px;top:1552px" width="22" height="22" viewBox="0 0 22 22"><circle cx="11" cy="11" r="10" fill="#f69f25"/><path d="M7 6 L9 6 L10 9 L8.5 10 Q10 13 12 13.5 L13 12 L16 13 L16 15 Q15 16.5 13 16 Q7.5 14 6 8.5 Q5.8 6.5 7 6 Z" fill="#fff"/></svg>
  <p class="abs contact" style="left:472px;top:1580px">07631 45 12 380</p>
  <div class="abs divider" style="left:632px"></div>
  <svg class="abs" style="left:723px;top:1552px" width="22" height="22" viewBox="0 0 22 22"><circle cx="11" cy="11" r="10" fill="#f69f25"/><g stroke="#fff" stroke-width="1.4" fill="none"><circle cx="11" cy="11" r="6"/><ellipse cx="11" cy="11" rx="2.5" ry="6"/><path d="M5 11 H17"/></g></svg>
  <p class="abs contact" style="left:654px;top:1578px">www.kavenor.de</p>
  <div class="abs divider" style="left:832px"></div>
  <svg class="abs" style="left:937px;top:1552px" width="22" height="22" viewBox="0 0 22 22"><circle cx="11" cy="11" r="10" fill="#f69f25"/><g stroke="#fff" stroke-width="1.4" fill="none"><rect x="5.5" y="7" width="11" height="8"/><path d="M5.5 7 L11 11.5 L16.5 7"/></g></svg>
  <p class="abs contact" style="left:849px;top:1578px">kontakt@kavenor.de</p>
</main>
</body>
</html>
```